Fire Department Recruitment Flyer

This is a recruitment piece. Would use the designs for social media ads and a postcard mailer design. Attached word document contains information needed on the design. Pictures attached. Do not have to use them all. This is focusing towards paramedics that will work on the ambulance in our Fire and EMS Department. Please include the Department Patch and QR Code that is attached.

```html
<!DOCTYPE html>
<html lang="en">
<head>
<meta charset="utf-8">
<title>Brookfield Fire & EMS – Now Hiring</title>
<link href="https://fonts.googleapis.com/css2?family=Montserrat:wght@700;800;900&family=Oswald:wght@500;600&display=swap" rel="stylesheet">
<style>
  :root{
    --page:#ffffff;
    --red:#a3212b;
    --red-dark:#7e1820;
    --slate:#4d5a63;
    --black:#0b0b0b;
    --gold:#f0bd1a;
    --gold-dark:#6b5a14;
    --white:#f4f4f4;
    --rule:#e7d3d3;
  }
  *{margin:0;padding:0;box-sizing:border-box}
  html,body{width:1200px;height:1200px;overflow:hidden;background:var(--page)}
  .flyer{position:absolute;left:200px;top:35px;width:800px;height:1130px;background:var(--black);overflow:hidden;font-family:"Montserrat",sans-serif}
  .layer{position:absolute;left:0;top:0}
  .header-rule{position:absolute;height:2px;background:var(--rule);width:267px}
  .headline{position:absolute;left:38px;width:267px;top:38px;text-align:center;color:var(--white);font-weight:900;font-size:62px;line-height:60px;letter-spacing:-3px}
  .dept-name{position:absolute;left:314px;width:172px;top:70px;text-align:center;color:var(--white);font-weight:800;font-size:21px;line-height:28px}
  .role{position:absolute;left:500px;width:267px;top:60px;text-align:center;color:var(--gold);font-weight:800;font-size:21px;line-height:29px}
  .role .levels{font-family:"Oswald",sans-serif;font-weight:500;color:var(--white);font-size:18px}
  .pay{position:absolute;left:38px;top:630px;width:724px;height:189px}
  .pay-title{position:absolute;left:0;width:724px;top:16px;text-align:center;color:var(--red);font-weight:900;font-size:56px;line-height:60px;letter-spacing:-0.5px}
  .pay-title .stars{font-size:42px;vertical-align:6px}
  .pay-range{position:absolute;left:0;width:724px;top:86px;text-align:center;color:var(--black);font-weight:800;font-size:47px;line-height:52px;letter-spacing:-0.5px}
  .pay-note{position:absolute;left:20px;top:145px;color:var(--black);font-weight:800;font-size:19px}
  .benefits-title{position:absolute;left:0;width:800px;top:836px;text-align:center;color:var(--red);font-weight:900;font-size:29px;letter-spacing:0.5px}
  .benefit{position:absolute;top:896px;width:180px;text-align:center}
  .benefit-label{color:var(--white);font-weight:800;font-size:14.5px;line-height:17px;height:52px}
  .benefit svg{display:block;margin:0 auto}
  .retire-mark{color:var(--gold);font-weight:800;font-size:44px;line-height:90px}
  .divider{position:absolute;top:920px;width:2px;height:130px;background:var(--white)}
  .footer-band{position:absolute;left:0;top:1091px;width:800px;height:39px;background:var(--red)}
</style>
</head>
<body>
<main class="flyer">
  <svg class="layer" width="800" height="640" viewBox="0 0 800 640">
    <defs>
      <linearGradient id="stationTone" x1="0" y1="0" x2="0" y2="1">
        <stop offset="0" stop-color="#8fb2d8"/>
        <stop offset="0.45" stop-color="#b5aa92"/>
        <stop offset="1" stop-color="#8f8d86"/>
      </linearGradient>
      <linearGradient id="crewTone" x1="0" y1="0" x2="0" y2="1">
        <stop offset="0" stop-color="#4a5468"/>
        <stop offset="1" stop-color="#1d2233"/>
      </linearGradient>
    </defs>
    <g role="img" aria-label="Photo of the fire station with engines and crew out front, and two smiling paramedics in uniform jackets">
      <polygon points="0,150 800,150 800,424 400,616 0,424" fill="url(#stationTone)"/>
      <rect x="38" y="267" width="234" height="363" rx="60" fill="url(#crewTone)"/>
      <rect x="507" y="217" width="256" height="413" rx="60" fill="url(#crewTone)"/>
    </g>
    <polyline points="0,424 400,616 800,424" fill="none" stroke="#f2f2f2" stroke-width="4"/>
    <polygon points="0,0 800,0 800,164 749,207 51,207 0,164" fill="var(--slate)"/>
    <polygon points="0,0 800,0 800,152 740,196 60,196 0,152" fill="var(--red)"/>
  </svg>

  <div class="header-rule" style="left:38px;top:26px"></div>
  <div class="header-rule" style="left:38px;top:31px"></div>
  <div class="header-rule" style="left:38px;top:166px"></div>
  <div class="header-rule" style="left:38px;top:171px"></div>
  <div class="header-rule" style="left:496px;top:26px"></div>
  <div class="header-rule" style="left:496px;top:31px"></div>
  <div class="header-rule" style="left:496px;top:166px"></div>
  <div class="header-rule" style="left:496px;top:171px"></div>

  <h1 class="headline">NOW<br>HIRING</h1>

  <p class="dept-name">BROOKFIELD<br>FIRE &amp; EMS</p>

  <p class="role">Full-time Certified<br>ALS PROVIDERS<br><span class="levels">(Intermediate and Paramedics)</span></p>

  <section class="pay">
    <svg class="layer" width="724" height="189" viewBox="0 0 724 189">
      <polygon points="0,0 724,0 724,133 668,189 0,189" fill="var(--gold)"/>
      <polygon points="668,189 668,133 724,133" fill="var(--gold-dark)"/>
      <polyline points="668,177 12,177 12,12 712,12 712,133" fill="none" stroke="var(--red)" stroke-width="2"/>
    </svg>
    <h2 class="pay-title"><span class="stars">***</span> STARTING PAY <span class="stars">***</span></h2>
    <p class="pay-range">$51,578.82 - $66,254.28</p>
    <p class="pay-note">Based on years of career experience and certification level</p>
  </section>

  <h3 class="benefits-title">FULL BENEFITS:</h3>

  <div class="benefit" style="left:39px">
    <p class="benefit-label">AFFORDABLE<br>INSURANCE</p>
    <svg width="96" height="100" viewBox="0 0 96 100" fill="none" stroke="var(--gold)" stroke-width="4" stroke-linejoin="round">
      <path d="M48 4 L80 16 V40 C80 60 66 72 48 80 C30 72 16 60 16 40 V16 Z"/>
      <path d="M48 14 L72 23 V40 C72 55 62 64 48 70 C34 64 24 55 24 40 V23 Z" stroke-width="2.5"/>
      <path d="M48 28 V54 M35 41 H61" stroke-width="6"/>
      <path d="M4 76 L20 76 L34 88 L62 84 L88 70 C92 68 94 74 90 76 L60 94 L30 96 L14 90 L4 90 Z"/>
    </svg>
  </div>
  <div class="benefit" style="left:220px">
    <p class="benefit-label">STATELINE<br>RETIREMENT<br>SYSTEM</p>
    <p class="retire-mark">SRS</p>
  </div>
  <div class="benefit" style="left:400px">
    <p class="benefit-label">PAID TIME<br>OFF</p>
    <svg width="100" height="90" viewBox="0 0 100 90" fill="none" stroke="var(--gold)" stroke-width="4" stroke-linejoin="round">
      <path d="M36 14 V6 H60 V14"/>
      <rect x="4" y="14" width="86" height="58" rx="10"/>
      <path d="M18 72 V80 M76 72 V80"/>
      <circle cx="76" cy="60" r="20" fill="var(--black)"/>
      <circle cx="76" cy="60" r="14" stroke-width="2.5"/>
      <path d="M76 50 V60 L83 64" stroke-width="3"/>
    </svg>
  </div>
  <div class="benefit" style="left:581px">
    <p class="benefit-label">YEARLY SALARY<br>INCREASE</p>
    <svg width="100" height="100" viewBox="0 0 100 100" fill="none" stroke="var(--gold)" stroke-width="4" stroke-linejoin="round">
      <text x="2" y="44" fill="var(--gold)" stroke="none" font-family="Montserrat, sans-serif" font-weight="900" font-size="42">$</text>
      <path d="M4 64 C40 56 66 40 84 14"/>
      <path d="M72 12 L86 8 L88 22"/>
      <rect x="4" y="72" width="24" height="24"/>
      <rect x="36" y="56" width="24" height="40"/>
      <rect x="68" y="30" width="24" height="66"/>
    </svg>
  </div>

  <span class="divider" style="left:219px"></span>
  <span class="divider" style="left:399px"></span>
  <span class="divider" style="left:580px"></span>

  <div class="footer-band"></div>
</main>
</body>
</html>
```